KTB - Redesign (PSD Files Only)

Requirements for the site:

1. We need our logo recreated, please use the same design and change colors to work on a white background

2. The site is a "Wizard" based site, that takes the customer through the process of creating a unique web presence that suits there needs

3.Colors Needed - Main "Dark Blue" Secondary = "Dark Grey" -Other = "Light Grey and White"

4.We need a CRISP CLEAN DESIGN, simple design

5.Wireframes are a general layout and may be modified by you to enhance the design

6. We want a complete web 5.0 look with big buttons and text boxes

7.The more personality the better

8. Current Site brightlarkworks.example

9.See attachments for wireframes

10. Designer should deliver PSD files, no coding is required

11. The portfolio wireframe, should look like the design of the pixelharbor portfolio template
Updates

KEEP IT SIMPLE.,.....

We like the moonquill scaffold style of designs

```html
<!DOCTYPE html>
<html lang="en">
<head>
<meta charset="utf-8">
<title>KTB Works Inc – Custom Website Design</title>
<link href="https://fonts.googleapis.com/css2?family=Dosis:wght@500;600;700&family=Open+Sans:wght@400;600;700&display=swap" rel="stylesheet">
<style>
:root{
  --navy:#0a2a52;
  --blue-deep:#06264a;
  --blue-mid:#0d4a86;
  --blue-glow:#1769b3;
  --ink:#1a3a66;
  --text:#222;
  --muted:#444;
  --line:#d8d8d8;
  --grey-bg:#d3d3d3;
  --dark:#1f1f1f;
  --darker:#141414;
  --orange:#f7770f;
  --orange-light:#ff9a2e;
  --white:#fff;
}
*{box-sizing:border-box;margin:0;padding:0}
html,body{width:1098px;height:1200px;overflow:hidden}
body{position:relative;font-family:"Open Sans",Arial,sans-serif;background:var(--grey-bg);color:var(--text)}
.hero{position:absolute;left:0;top:0;width:1098px;height:475px;
  background:radial-gradient(ellipse 340px 300px at 549px 250px,var(--blue-glow) 0%,var(--blue-mid) 45%,var(--blue-deep) 100%)}
.topnav{position:absolute;left:172px;top:0;width:756px;height:37px;background:var(--darker);display:flex;align-items:center}
.topnav a{font-family:"Dosis",sans-serif;font-weight:500;font-size:17px;color:var(--white);text-decoration:none;padding:0 7px;line-height:37px}
.topnav a:first-child{margin-left:12px}
.topnav a.active{background:var(--blue-mid);padding:0 11px}
.social{display:flex;gap:6px}
.social span{display:block;width:20px;height:20px;border-radius:50%;background:var(--white)}
.topnav .social{position:absolute;left:409px;top:8px}
.phone{display:flex;align-items:center;gap:4px;font-family:"Dosis",sans-serif;color:var(--white)}
.topnav .phone{position:absolute;right:14px;top:6px;font-size:20px}
.headline{position:absolute;top:64px;width:1098px;text-align:center;font-family:"Dosis",sans-serif;font-weight:700;font-size:29px;color:var(--white)}
.lede{position:absolute;top:106px;left:190px;width:718px;text-align:center;font-size:14px;line-height:16.5px;color:var(--white)}
.badge{position:absolute;border-radius:50%;background:var(--blue-deep);display:flex;align-items:center;justify-content:center;text-align:center;color:var(--white);font-size:13.5px;line-height:18px;box-shadow:0 0 0 4px rgba(255,255,255,.05)}
.badge.small{width:108px;height:108px}
.badge .arc{position:absolute;left:-6px;top:-6px;width:120px;height:120px}
.stem{position:absolute;width:1px;background:rgba(255,255,255,.25)}
.logo{position:absolute;left:459px;top:163px;width:180px;height:180px;border-radius:50%;background:var(--blue-deep);display:flex;align-items:center;justify-content:center;font-family:"Dosis",sans-serif;font-weight:700;font-size:50px;color:var(--white);letter-spacing:2px}
.step{position:absolute;left:474px;top:368px;width:151px;text-align:center;font-family:"Dosis",sans-serif;font-weight:500;font-size:21px;color:var(--white)}
.step-track{position:absolute;left:474px;top:402px;width:151px;height:2px;background:var(--blue-deep)}
.step-track i{display:block;width:37px;height:2px;background:var(--white)}
.starter{position:absolute;left:220px;top:449px;width:658px;height:51px;background:#efefef;border:1px solid #cfcfcf}
.starter input{position:absolute;left:0;top:0;width:455px;height:49px;border:0;background:transparent;padding-left:20px;font-family:"Open Sans",sans-serif;font-size:15px;color:#888}
.btn{font-family:"Dosis",sans-serif;font-weight:700;color:var(--white);background:linear-gradient(var(--orange-light),var(--orange));border:0;display:flex;align-items:center;justify-content:center}
.starter .btn{position:absolute;left:458px;top:3px;width:196px;height:44px;font-size:22px}
.services{position:absolute;left:172px;top:532px;width:755px;height:443px;background:var(--white);border:1px solid #c4c4c4;display:flex}
.card{position:relative;flex:1;border-right:1px solid #dedede;padding:0 20px}
.card:last-child{border-right:0}
.card .icon{position:absolute;left:20px;top:34px;width:66px;height:66px}
.card h2{position:absolute;top:120px;font-family:"Dosis",sans-serif;font-weight:600;font-size:17px;color:var(--ink)}
.card p{position:absolute;top:149px;left:20px;right:12px;font-weight:700;font-size:11px;line-height:14px;letter-spacing:-.2px;color:#111}
.card ul{position:absolute;top:204px;left:20px;right:18px;list-style:none}
.card li{font-size:10.2px;line-height:13px;padding:5px 0 5px 11px;border-bottom:1px dashed var(--line);position:relative;color:var(--muted)}
.card li:last-child{border-bottom:0}
.card li::before{content:"›";position:absolute;left:1px;top:3px;font-weight:700;font-size:12px;color:#333}
.more{position:absolute;top:380px;left:22px;display:flex;align-items:center;gap:7px;font-size:10.5px;color:var(--ink)}
.more .ring{width:27px;height:27px;border-radius:50%;border:1.6px solid var(--ink);display:flex;align-items:center;justify-content:center}
.more.hot{color:var(--orange)}
.more.hot .ring{border-color:var(--orange)}
.footer{position:absolute;left:0;top:1012px;width:1098px;height:188px;background:var(--dark)}
.footer-links{position:absolute;left:172px;top:33px;font-size:10px;line-height:15.5px;color:var(--white)}
.footer-links u{text-decoration:underline}
.footer .social{position:absolute;left:467px;top:30px;gap:5px}
.footer .social span{width:31px;height:31px}
.footer .phone{position:absolute;left:467px;top:67px;font-size:21px}
.footer .btn{position:absolute;left:732px;top:30px;width:194px;height:44px;font-size:21px}
.strip{position:absolute;left:172px;top:98px;width:760px;height:44px;background:var(--darker)}
.partner{position:absolute;left:0;top:0;width:125px;height:44px;background:var(--white);display:flex}
.partner i{display:block;width:43px;height:44px;background:#2f67c8}
</style>
</head>
<body>
<header class="hero">
  <nav class="topnav">
    <a href="#">Home</a><a href="#" class="active">About Us</a><a href="#">Portfolio</a><a href="#">Contact Us</a>
    <div class="social" aria-label="Social links"><span></span><span></span><span></span><span></span></div>
    <div class="phone"><svg width="12" height="14" viewBox="0 0 12 14"><path d="M3 1l2 3-1.3 1.3c.6 1.7 1.7 3 3.3 3.9L8.3 8 11 10l-1.2 2.6C5 12 1.5 7.5 1.2 2.3z" fill="#fff"/></svg>1800-555-0142</div>
  </nav>
  <h1 class="headline">Get a Custome Website Design in 21 Days or LESS !</h1>
  <p class="lede">Find out why we're the #1 custom website design marketplace. Our network of designers will create 50+ web design samples for you to choose and our marketing experts will pave the way your success.</p>

  <div class="stem" style="left:250px;top:304px;height:171px"></div>
  <div class="stem" style="left:372px;top:399px;height:76px"></div>
  <div class="stem" style="left:728px;top:396px;height:79px"></div>
  <div class="stem" style="left:846px;top:304px;height:171px"></div>

  <div class="badge small" style="left:196px;top:196px">24x7<br>customer<br>support
    <svg class="arc" viewBox="0 0 120 120"><path d="M4 84a60 60 0 0 0 112 0" fill="none" stroke="#0f477f" stroke-width="3"/></svg></div>
  <div class="badge small" style="left:318px;top:291px">100% No<br>Obligation<br>Free Web<br>Quote
    <svg class="arc" viewBox="0 0 120 120"><path d="M4 84a60 60 0 0 0 112 0" fill="none" stroke="#0f477f" stroke-width="3"/></svg></div>
  <div class="badge small" style="left:674px;top:288px">Save<br>100% on<br>Webdesign
    <svg class="arc" viewBox="0 0 120 120"><path d="M4 84a60 60 0 0 0 112 0" fill="none" stroke="#0f477f" stroke-width="3"/></svg></div>
  <div class="badge small" style="left:792px;top:196px">100%<br>Momeyback<br>Guarantee
    <svg class="arc" viewBox="0 0 120 120"><path d="M4 84a60 60 0 0 0 112 0" fill="none" stroke="#0f477f" stroke-width="3"/></svg></div>

  <div class="logo">KTB</div>
  <svg style="position:absolute;left:294px;top:402px" width="32" height="32" viewBox="0 0 32 32"><path d="M28 3C18 4 11 12 7 28" fill="none" stroke="rgba(255,255,255,.5)" stroke-width="1.2"/><path d="M3 23l4 6 3-6" fill="none" stroke="rgba(255,255,255,.5)" stroke-width="1.2"/></svg>
  <div class="step">STEP 1</div>
  <div class="step-track"><i></i></div>

  <form class="starter">
    <input type="text" placeholder="Name your project">
    <span class="btn">Get Started Now</span>
  </form>
</header>

<main class="services">
  <section class="card">
    <svg class="icon" viewBox="0 0 66 66"><path d="M21 44c-4-5-8-9-8-17a20 20 0 0 1 40 0c0 8-4 12-8 17v5H21z" fill="none" stroke="#1a3a66" stroke-width="2.5"/><path d="M28 44V30l-4-6M38 44V30l4-6M28 30q5 5 10 0" fill="none" stroke="#1a3a66" stroke-width="2"/><rect x="23" y="51" width="20" height="4" fill="#1a3a66"/><rect x="25" y="57" width="16" height="4" fill="#1a3a66"/></svg>
    <h2>Why Choose KTB ?</h2>
    <p>We are a full service design &amp; marketing company that will handle everything.</p>
    <ul><li>Dedicated Project Manager</li><li>Single Point of Contact</li><li>Marketing Coaches</li><li>Low Cost</li><li>50+ Design Sample for you to choose</li></ul>
    <a class="more hot"><span class="ring"><svg width="10" height="8" viewBox="0 0 10 8"><path d="M0 2.5h5V0l5 4-5 4V5.5H0z" fill="#f7770f"/></svg></span>Learn More</a>
  </section>
  <section class="card">
    <svg class="icon" viewBox="0 0 66 66" role="img" aria-label="Globe icon"><circle cx="33" cy="33" r="32" fill="#1a3a66"/><circle cx="33" cy="33" r="27" fill="none" stroke="#fff" stroke-width="1.5"/></svg>
    <h2>Web Services</h2>
    <p>We specialize in the following design services</p>
    <ul><li>web Design</li><li>Ecommerce Design</li><li>Web Programming</li><li>Logo Design</li><li>Stationary / Print Design</li><li>Ad Design</li><li>Email Template Design.</li></ul>
    <a class="more"><span class="ring"><svg width="10" height="8" viewBox="0 0 10 8"><path d="M0 2.5h5V0l5 4-5 4V5.5H0z" fill="#1a3a66"/></svg></span>Learn More</a>
  </section>
  <section class="card">
    <svg class="icon" viewBox="0 0 66 66"><path d="M3 8v52h48" fill="none" stroke="#1a3a66" stroke-width="5"/><path d="M14 44V26l8 14 12-24" fill="none" stroke="#1a3a66" stroke-width="3"/></svg>
    <h2>Maketing Services</h2>
    <p>We handle all online markeing including the following.</p>
    <ul><li>Searchly Ads</li><li>Searchly Local Marketing</li><li>Search Engine Optimization</li><li>Email Marketing</li><li>Social Media Marketing</li></ul>
    <a class="more"><span class="ring"><svg width="10" height="8" viewBox="0 0 10 8"><path d="M0 2.5h5V0l5 4-5 4V5.5H0z" fill="#1a3a66"/></svg></span>Learn More</a>
  </section>
  <section class="card">
    <svg class="icon" viewBox="0 0 66 66"><g fill="#1a3a66"><circle cx="22" cy="22" r="14"/><g stroke="#1a3a66" stroke-width="6"><path d="M22 3v38M3 22h38M9 9l26 26M35 9L9 35"/></g><circle cx="44" cy="46" r="9"/><g stroke="#1a3a66" stroke-width="4"><path d="M44 33v26M31 46h26M35 37l18 18M53 37L35 55"/></g></g><circle cx="22" cy="22" r="6" fill="#fff"/><circle cx="44" cy="46" r="4" fill="#fff"/></svg>
    <h2>Maintainence Services</h2>
    <p>Let us maintain your site and save up to 50% on the following :</p>
    <ul><li>Website Hosting</li><li>Software Upgrades</li><li>Custom Web Programming</li><li>Website Marketing</li></ul>
    <a class="more"><span class="ring"><svg width="10" height="8" viewBox="0 0 10 8"><path d="M0 2.5h5V0l5 4-5 4V5.5H0z" fill="#1a3a66"/></svg></span>Learn More</a>
  </section>
</main>

<footer class="footer">
  <div class="footer-links">Home &nbsp;. &nbsp;<u>About Us</u> &nbsp;. &nbsp;Portfolio &nbsp;. &nbsp;Contact Us<br>Copyright © 2014 KTB Works Inc - All Right Reserved<br>www.brightlarkworks.example</div>
  <div class="social" aria-label="Social links"><span></span><span></span><span></span><span></span></div>
  <div class="phone"><svg width="12" height="14" viewBox="0 0 12 14"><path d="M3 1l2 3-1.3 1.3c.6 1.7 1.7 3 3.3 3.9L8.3 8 11 10l-1.2 2.6C5 12 1.5 7.5 1.2 2.3z" fill="#fff"/></svg>1800-555-0142</div>
  <span class="btn">Request Consultant</span>
  <div class="strip"><div class="partner" role="img" aria-label="Partner badge"><i></i></div></div>
</footer>
</body>
</html>
```